Corporate Trainning business needs PPT template for sales, reports and projects

Create a power point template with own design and rich in distinctness of our brand, logo and industry (corporate training). Enough slides templates to use for sales, reports and projects development: flowcharts, roadmaps, bullets, service categories, description box, title & subtitle slides, bar & pie charts, calendars, gantt, some basic shapes and icons (training, education, elearning, etc related).
Enclose: color palette, set of logo for different uses and ppt presentation with some ideas and slide templates. The ppt hope could help, but I trust in your experience and creativity.

Target Market(s)

Company training

Industry/Entity Type

Training - Education

Font styles to use
Sans Serif

Requirements
Nice to have
• Relative to training icons

```html
<!DOCTYPE html>
<html lang="en">
<head>
<meta charset="utf-8">
<title>Corvanta – Presentation Template</title>
<link rel="stylesheet" href="https://fonts.googleapis.com/css2?family=Montserrat:wght@300;400;500;600;700;800&display=swap">
<style>
:root{
  --navy:#0d2c5a;
  --yellow:#f1c400;
  --teal:#0a8aad;
  --teal-light:#7ccfe0;
  --grey:#6b6b6b;
  --text:#2b2b2b;
  --muted:#8a8a8a;
  --page:#e7e8ea;
  --panel:#f3f4f5;
  --white:#ffffff;
}
*{box-sizing:border-box;margin:0;padding:0}
html,body{width:1200px;height:2448px;overflow:hidden}
body{font-family:"Montserrat",Arial,sans-serif;background:var(--page);color:var(--text);position:relative}

/* hero area */
.hero{position:absolute;left:0;top:0;width:1200px;height:740px;background:linear-gradient(180deg,#d9dce2 0%,#eef0f2 70%,#e7e8ea 100%)}
.hero-brand{position:absolute;left:910px;top:56px;display:flex;align-items:center;gap:14px}
.hero-brand .dot{width:56px;height:56px;border-radius:50%;background:var(--yellow)}
.hero-brand .name{font-size:48px;font-weight:500;color:var(--navy)}
.hero-slide{position:absolute;left:150px;top:190px;transform:scale(1.3);transform-origin:0 0;box-shadow:0 14px 40px rgba(0,0,0,.18)}

/* slides */
.slide{position:absolute;width:562px;height:316px;background:var(--white);overflow:hidden}
.col-l{left:28px}.col-r{left:609px}
.row-1{top:759px}.row-2{top:1094px}.row-3{top:1429px}.row-4{top:1764px}.row-5{top:2099px}

.slide-title{position:absolute;left:22px;top:23px;display:flex;align-items:center;gap:14px;font-size:16px;color:var(--navy);font-weight:400}
.slide-title::before{content:"";width:5px;height:22px;background:var(--yellow);border-radius:2px}
.slide-title b{font-weight:700}

.brand{display:flex;align-items:center;gap:5px}
.brand .dot{border-radius:50%;background:var(--yellow)}
.brand .name{font-weight:500;color:var(--navy)}
.foot-brand{position:absolute;left:14px;bottom:12px}
.foot-brand .dot{width:15px;height:15px}
.foot-brand .name{font-size:16px}
.foot-copy{position:absolute;right:16px;bottom:15px;display:flex;align-items:center;gap:8px;font-size:5px;color:var(--grey)}
.foot-copy .pg{display:flex;align-items:center;gap:8px;color:var(--yellow);font-weight:700;font-size:6px}
.foot-copy .pg::before{content:"";width:2px;height:9px;background:var(--teal)}

.copy-bar{position:absolute;left:0;bottom:0;width:100%;height:20px;background:var(--teal);color:var(--white);font-size:6px;display:flex;align-items:center;justify-content:center}

.photo{position:absolute}
.icon{border-radius:50%;display:flex;align-items:center;justify-content:center}
.icon svg{width:55%;height:55%}
.bg-navy{background:var(--navy)}.bg-yellow{background:var(--yellow)}.bg-teal{background:var(--teal)}

.lorem{font-size:6px;line-height:1.2;color:var(--muted)}

/* title slide */
.title-photo{left:250px;top:0;width:312px;height:296px;border-bottom-left-radius:300px 296px;background:linear-gradient(135deg,#f4f6f9 0%,#dfe5ec 45%,#c9d5e0 100%)}
.title-accent{position:absolute;left:476px;top:166px;width:90px;height:95px;border-radius:22px;background:var(--yellow);opacity:.85}
.title-brand{position:absolute;left:30px;top:32px}
.title-brand .dot{width:30px;height:30px}
.title-brand .name{font-size:28px}
.title-band{position:absolute;left:0;top:101px;width:310px;height:118px;background:var(--navy);border-radius:0 32px 32px 0;padding:18px 0 0 30px}
.title-band .kicker{font-size:27px;font-weight:800;color:var(--yellow);letter-spacing:.3px;line-height:1}
.title-band .main{font-size:27px;font-weight:400;color:var(--yellow);line-height:1.15}
.title-band .sub{font-size:11px;color:var(--white);margin-top:10px}
.title-date{position:absolute;left:30px;top:256px;font-size:6.5px;color:var(--grey)}

/* solutions */
.sol-grid{position:absolute;left:20px;top:71px;width:524px;display:grid;grid-template-columns:repeat(3,1fr);row-gap:16px}
.sol-item{text-align:center}
.sol-item .icon{width:36px;height:36px;margin:0 auto 6px}
.sol-item h3{font-size:11px;font-weight:400;color:var(--text)}
.sol-item h3 b{font-weight:700}
.sol-item p{font-size:6px;color:var(--muted);line-height:1.15;width:135px;margin:2px auto 0}

/* values */
.values{position:absolute;left:77px;top:71px}
.value{display:flex;gap:12px;align-items:flex-start;margin-bottom:14px}
.value .icon{width:50px;height:50px;flex:none}
.value h3{font-size:11px;font-weight:400;margin-top:3px}
.value h3 b{font-weight:700}
.value p{font-size:6px;color:var(--muted);line-height:1.2;width:340px;margin-top:5px}

/* features */
.feat-panel{position:absolute;left:0;top:0;width:282px;height:316px;background:var(--navy)}
.feat-panel .slide-title{color:var(--white)}
.feat-list{position:absolute;left:41px;top:77px}
.feat{display:flex;gap:13px;align-items:center;margin-bottom:11px}
.feat .icon{width:36px;height:36px;flex:none}
.feat h3{font-size:11px;font-weight:400;color:var(--yellow)}
.feat h3 b{font-weight:700}
.feat p{font-size:6px;color:#c9d2e0;line-height:1.15;width:140px;margin-top:2px}
.feat-photo{left:291px;top:9px;width:263px;height:272px;background:linear-gradient(140deg,#c4ccd3 0%,#8c99a3 50%,#3a4650 100%)}
.on-dark .name{color:var(--white)}

/* process */
.proc-photo{left:9px;top:9px;width:264px;height:256px;background:linear-gradient(160deg,#9b7a5a 0%,#c9b49b 40%,#dfe2e4 70%,#b2926f 100%)}
.proc-panel{position:absolute;left:282px;top:0;width:280px;height:316px;background:var(--panel)}
.proc-panel .slide-title{left:16px}
.steps{position:absolute;left:16px;top:77px}
.step{display:flex;align-items:flex-start;height:49px}
.step .date{width:70px;text-align:right;font-size:8px;font-weight:700;color:var(--teal);padding-top:2px}
.step .mark{width:6px;height:6px;background:var(--yellow);margin:3px 14px 0 18px;flex:none}
.step h3{font-size:11px;font-weight:700;color:var(--navy)}
.step h3 span{font-weight:400}
.step p{font-size:6px;color:var(--muted);line-height:1.15;width:115px;margin-top:2px}

/* infographics */
.info-text{position:absolute;font-size:6px;line-height:1.2;color:var(--muted)}
.info-text.barred{padding-left:8px;border-left:4px solid var(--navy)}
.info-text h3{font-size:11px;font-weight:400;color:var(--text);margin-bottom:3px}
.info-text h3 b{font-weight:700}
.chart{position:absolute;left:0;top:0}

/* table */
.data-table{position:absolute;left:36px;top:78px;width:489px;border-collapse:collapse;font-size:8px}
.data-table th{height:28px;font-weight:700;color:var(--white);text-align:center;font-size:8px}
.data-table th:first-child{text-align:left;padding-left:4px;background:var(--navy)}
.data-table th.c1{background:var(--yellow);color:var(--navy)}
.data-table th.c2{background:var(--teal)}
.data-table th.c3{background:var(--teal-light);color:var(--teal)}
.data-table th.c4{background:#6d6e70}
.data-table td{height:29px;text-align:center;border-right:1px solid #e4e4e4}
.data-table td:first-child{text-align:left;padding-left:4px;font-weight:700;color:var(--text)}
.data-table tr:nth-child(even) td{background:#f4f4f4}
.yes{color:#2da24a;font-weight:700}
.no{color:#d92c2c;font-weight:700}

/* chart slide */
.options{position:absolute;left:345px;top:90px}
.option{display:flex;gap:12px;align-items:center;margin-bottom:22px}
.option .icon{width:38px;height:38px;flex:none}
.option h3{font-size:11px;font-weight:400}
.option h3 b{font-weight:700}
.option p{font-size:6px;color:var(--muted);line-height:1.15;width:120px;margin-top:2px}

/* contact */
.contact-photo{left:244px;top:0;width:318px;height:296px;border-bottom-left-radius:260px 296px;border-top-left-radius:200px 296px;background:linear-gradient(160deg,#cdd3d8 0%,#6e7c86 45%,#2c3a44 100%)}
.contact-accent{position:absolute;left:470px;top:180px;width:95px;height:100px;border-radius:24px;background:var(--yellow);opacity:.6}
.contact-brand{position:absolute;left:36px;top:118px}
.contact-brand .dot{width:34px;height:34px}
.contact-brand .name{font-size:32px}
.contact-list{position:absolute;left:40px;top:196px}
.contact-list h3{font-size:11px;font-weight:700;color:var(--navy);margin-bottom:9px}
.contact-list li{list-style:none;display:flex;gap:9px;align-items:center;font-size:7px;color:var(--grey);margin-bottom:5px}
.contact-list svg{width:9px;height:9px}
</style>
</head>
<body>

<!-- hero -->
<section class="hero">
  <div class="hero-brand brand"><span class="dot"></span><span class="name">Corvanta</span></div>

  <div class="slide hero-slide">
    <div class="photo title-photo" role="img" aria-label="Photo of a hand drawing a line chart with a blue pen"></div>
    <div class="title-accent"></div>
    <div class="title-brand brand"><span class="dot"></span><span class="name">Corvanta</span></div>
    <div class="title-band">
      <div class="kicker">PRESENTATION</div>
      <div class="main">Title Goes Here!</div>
      <div class="sub">Presentation Subtitle Goes Here!</div>
    </div>
    <div class="title-date">Saturday, August 13, 2022</div>
    <div class="copy-bar">© 2022 Corvanta Learning. All rights reserved.</div>
  </div>
</section>

<!-- 1 title -->
<section class="slide col-l row-1">
  <div class="photo title-photo" role="img" aria-label="Photo of a hand drawing a line chart with a blue pen"></div>
  <div class="title-accent"></div>
  <div class="title-brand brand"><span class="dot"></span><span class="name">Corvanta</span></div>
  <div class="title-band">
    <div class="kicker">PRESENTATION</div>
    <div class="main">Title Goes Here!</div>
    <div class="sub">Presentation Subtitle Goes Here!</div>
  </div>
  <div class="title-date">Saturday, August 13, 2022</div>
  <div class="copy-bar">© 2022 Corvanta Learning. All rights reserved.</div>
</section>

<!-- 2 solutions -->
<section class="slide col-r row-1">
  <h2 class="slide-title"><span><b>Corvanta</b> Solutions</span></h2>
  <div class="sol-grid">
    <div class="sol-item"><div class="icon bg-navy"><svg viewBox="0 0 20 20"><circle cx="10" cy="8" r="5" fill="#fff"/><rect x="8" y="13" width="4" height="4" fill="#fff"/></svg></div><h3><b>Heading</b> Goes Here</h3><p>Vivamus eu dui ex. Curabitur dapibus dignissim dui, in molest</p></div>
    <div class="sol-item"><div class="icon bg-yellow"><svg viewBox="0 0 20 20"><path d="M15 3 L8 10 L10 12 L17 5 Z M6 11 L4 14 L9 16 Z" fill="#fff"/></svg></div><h3><b>Heading</b> Goes Here</h3><p>Vivamus eu dui ex. Curabitur dapibus dignissim dui, in molest</p></div>
    <div class="sol-item"><div class="icon bg-teal"><svg viewBox="0 0 20 20"><circle cx="8" cy="8" r="5" fill="none" stroke="#fff" stroke-width="2.5"/><path d="M12 12 L17 17" stroke="#fff" stroke-width="3"/></svg></div><h3><b>Heading</b> Goes Here</h3><p>Vivamus eu dui ex. Curabitur dapibus dignissim dui, in molest</p></div>
    <div class="sol-item"><div class="icon bg-teal"><svg viewBox="0 0 20 20"><circle cx="10" cy="10" r="7" fill="none" stroke="#fff" stroke-width="1.8"/><path d="M10 6 V10 H13" fill="none" stroke="#fff" stroke-width="1.8"/></svg></div><h3><b>Heading</b> Goes Here</h3><p>Vivamus eu dui ex. Curabitur dapibus dignissim dui, in molest</p></div>
    <div class="sol-item"><div class="icon bg-navy"><svg viewBox="0 0 20 20"><circle cx="6" cy="8" r="2.5" fill="#fff"/><circle cx="14" cy="8" r="2.5" fill="#fff"/><circle cx="10" cy="7" r="3" fill="#fff"/><rect x="3" y="12" width="14" height="4" rx="2" fill="#fff"/></svg></div><h3><b>Heading</b> Goes Here</h3><p>Vivamus eu dui ex. Curabitur dapibus dignissim dui, in molest</p></div>
    <div class="sol-item"><div class="icon bg-yellow"><svg viewBox="0 0 20 20"><rect x="4" y="11" width="3" height="6" fill="#fff"/><rect x="9" y="8" width="3" height="9" fill="#fff"/><rect x="14" y="5" width="3" height="12" fill="#fff"/></svg></div><h3><b>Heading</b> Goes Here</h3><p>Vivamus eu dui ex. Curabitur dapibus dignissim dui, in molest</p></div>
  </div>
  <div class="foot-brand brand"><span class="dot"></span><span class="name">Corvanta</span></div>
  <div class="foot-copy">© 2022 Corvanta Learning. All rights reserved.<span class="pg">2</span></div>
</section>

<!-- 3 values -->
<section class="slide col-l row-2">
  <h2 class="slide-title"><span><b>Corvanta</b> Values</span></h2>
  <div class="values">
    <div class="value"><div class="icon bg-navy"><svg viewBox="0 0 20 20"><path d="M8 3 H12 V8 L16 16 H4 L8 8 Z" fill="#fff"/></svg></div><div><h3>we love <b>innovations</b></h3><p>Lorem ipsum dolor sit amet, consectetur adipiscing elit. Vivamus eu dui ex. Curabitur dapibus dignissim dui, in molestie metus feugiat sed. Praesent aliquet lorem ex, eu dapibus odio varius at. Duis eget tellus porta, consequat lacus vitae, venenatis dolor.</p></div></div>
    <div class="value"><div class="icon bg-yellow"><svg viewBox="0 0 20 20"><circle cx="10" cy="8" r="6" fill="#fff"/><rect x="9" y="12" width="2" height="6" fill="#fff"/></svg></div><div><h3>we respect the <b>nature</b></h3><p>Lorem ipsum dolor sit amet, consectetur adipiscing elit. Vivamus eu dui ex. Curabitur dapibus dignissim dui, in molestie metus feugiat sed. Praesent aliquet lorem ex, eu dapibus odio varius at. Duis eget tellus porta, consequat lacus vitae, venenatis dolor.</p></div></div>
    <div class="value"><div class="icon bg-teal"><svg viewBox="0 0 20 20"><path d="M15 3 L8 10 L10 12 L17 5 Z M6 11 L4 14 L9 16 Z" fill="#fff"/></svg></div><div><h3>we believe in <b>future</b></h3><p>Lorem ipsum dolor sit amet, consectetur adipiscing elit. Vivamus eu dui ex. Curabitur dapibus dignissim dui, in molestie metus feugiat sed. Praesent aliquet lorem ex, eu dapibus odio varius at. Duis eget tellus porta, consequat lacus vitae, venenatis dolor.</p></div></div>
  </div>
  <div class="foot-brand brand"><span class="dot"></span><span class="name">Corvanta</span></div>
  <div class="foot-copy">© 2022 Corvanta Learning. All rights reserved.<span class="pg">3</span></div>
</section>

<!-- 4 features -->
<section class="slide col-r row-2">
  <div class="feat-panel">
    <h2 class="slide-title"><span><b>Heading</b> Goes Here!</span></h2>
    <div class="feat-list">
      <div class="feat"><div class="icon bg-yellow"><svg viewBox="0 0 20 20"><rect x="5" y="9" width="10" height="8" rx="1" fill="#fff"/><path d="M7 9 V6 a3 3 0 0 1 6 0 V9" fill="none" stroke="#fff" stroke-width="2"/></svg></div><div><h3>Feature <b>One</b></h3><p>Vivamus eu dui ex. Curabitur dapibus dignissim dui, in molestie metus.</p></div></div>
      <div class="feat"><div class="icon bg-yellow"><svg viewBox="0 0 20 20"><rect x="4" y="11" width="3" height="6" fill="#fff"/><rect x="9" y="8" width="3" height="9" fill="#fff"/><rect x="14" y="5" width="3" height="12" fill="#fff"/></svg></div><div><h3>Feature <b>Two</b></h3><p>Vivamus eu dui ex. Curabitur dapibus dignissim dui, in molestie metus.</p></div></div>
      <div class="feat"><div class="icon bg-yellow"><svg viewBox="0 0 20 20"><circle cx="10" cy="10" r="7" fill="none" stroke="#fff" stroke-width="1.8"/><path d="M10 6 V10 H13" fill="none" stroke="#fff" stroke-width="1.8"/></svg></div><div><h3>Feature <b>Three</b></h3><p>Vivamus eu dui ex. Curabitur dapibus dignissim dui, in molestie metus.</p></div></div>
      <div class="feat"><div class="icon bg-yellow"><svg viewBox="0 0 20 20"><rect x="5" y="9" width="10" height="8" rx="1" fill="#fff"/><path d="M7 9 V6 a3 3 0 0 1 6 -1" fill="none" stroke="#fff" stroke-width="2"/></svg></div><div><h3>Feature <b>Four</b></h3><p>Vivamus eu dui ex. Curabitur dapibus dignissim dui, in molestie metus.</p></div></div>
    </div>
    <div class="foot-brand brand on-dark"><span class="dot"></span><span class="name">Corvanta</span></div>
  </div>
  <div class="photo feat-photo" role="img" aria-label="Photo of a business meeting with a tablet showing a stock chart"></div>
  <div class="foot-copy">© 2022 Corvanta Learning. All rights reserved.<span class="pg">4</span></div>
</section>

<!-- 5 process -->
<section class="slide col-l row-3">
  <div class="photo proc-photo" role="img" aria-label="Top-down photo of a team working around a table with charts and laptops"></div>
  <div class="proc-panel">
    <h2 class="slide-title"><span>Four Steps <b>Process</b></span></h2>
    <div class="steps">
      <div class="step"><div class="date">JUN 01</div><span class="mark"></span><div><h3>Start <span>Point</span></h3><p>Vivamus eu dui ex. Curabitur dapibus dignissim dui, in molest</p></div></div>
      <div class="step"><div class="date">JUL 15</div><span class="mark"></span><div><h3>Midpoint <span>One</span></h3><p>Vivamus eu dui ex. Curabitur dapibus dignissim dui, in molest</p></div></div>
      <div class="step"><div class="date">AUG 01</div><span class="mark"></span><div><h3>Midpoint <span>Two</span></h3><p>Vivamus eu dui ex. Curabitur dapibus dignissim dui, in molest</p></div></div>
      <div class="step"><div class="date">SEP 15</div><span class="mark"></span><div><h3>Finish</h3><p>Vivamus eu dui ex. Curabitur dapibus dignissim dui, in molest</p></div></div>
    </div>
  </div>
  <div class="foot-brand brand"><span class="dot"></span><span class="name">Corvanta</span></div>
  <div class="foot-copy">© 2022 Corvanta Learning. All rights reserved.<span class="pg">5</span></div>
</section>

<!-- 6 branding venn -->
<section class="slide col-r row-3">
  <h2 class="slide-title"><span><b>Branding</b> Infographics</span></h2>
  <p class="info-text" style="left:41px;top:66px;width:160px">Marketing is the study and management of exchange relationships. Marketing is the business process of creating relationships with and satisfying customers.</p>
  <svg class="chart" width="562" height="316" viewBox="0 0 562 316">
    <circle cx="282" cy="150" r="60" fill="var(--navy)" stroke="#fff" stroke-width="3"/>
    <circle cx="247" cy="201" r="60" fill="var(--teal)" stroke="#fff" stroke-width="3"/>
    <circle cx="317" cy="201" r="60" fill="var(--yellow)" stroke="#fff" stroke-width="3"/>
    <circle cx="282" cy="179" r="31" fill="#4a5977" stroke="#fff" stroke-width="3"/>
    <ellipse cx="244" cy="159" rx="7" ry="4.5" fill="none" stroke="#fff" stroke-width="1.5"/><circle cx="244" cy="159" r="2" fill="#fff"/>
    <rect x="313" y="153" width="12" height="9" fill="none" stroke="#fff" stroke-width="1.3"/>
    <path d="M287 211 L280 218" stroke="#fff" stroke-width="2.5"/>
    <text x="282" y="118" font-size="6.5" fill="#fff" text-anchor="middle" font-family="Montserrat, sans-serif">Visual Identity</text>
    <text x="219" y="212" font-size="6.5" fill="#fff" text-anchor="middle" font-family="Montserrat, sans-serif">Brand Tone</text>
    <text x="345" y="212" font-size="6.5" fill="#fff" text-anchor="middle" font-family="Montserrat, sans-serif">Strategy</text>
  </svg>
  <p class="info-text barred" style="left:352px;top:104px;width:130px;border-color:var(--navy)">Lorem ipsum dolor sit amet, consectetur adipiscing elit. Vivamus eu dui ex. Curabitur dapibus</p>
  <p class="info-text" style="left:50px;top:202px;width:138px;text-align:right;padding-right:8px;border-right:4px solid var(--teal)">Lorem ipsum dolor sit amet, consectetur adipiscing elit. Vivamus eu dui ex. Curabitur dapibus</p>
  <p class="info-text barred" style="left:384px;top:202px;width:130px;border-color:var(--yellow)">Lorem ipsum dolor sit amet, consectetur adipiscing elit. Vivamus eu dui ex. Curabitur dapibus</p>
  <div class="foot-brand brand"><span class="dot"></span><span class="name">Corvanta</span></div>
  <div class="foot-copy">© 2022 Corvanta Learning. All rights reserved.<span class="pg">6</span></div>
</section>

<!-- 7 donut -->
<section class="slide col-l row-4">
  <h2 class="slide-title"><span>Creative <b>Infographics</b></span></h2>
  <svg class="chart" width="562" height="316" viewBox="0 0 562 316">
    <g transform="translate(282,170)" fill="none" stroke-width="46">
      <circle r="56" stroke="var(--navy)" stroke-dasharray="112.4 400" transform="rotate(-75)"/>
      <circle r="56" stroke="var(--yellow)" stroke-dasharray="112.4 400" transform="rotate(45)"/>
      <circle r="56" stroke="var(--teal)" stroke-dasharray="112.4 400" transform="rotate(165)"/>
    </g>
    <path d="M334 145 a6 6 0 0 1 12 0 v6 h3 h-18 h3 Z" fill="none" stroke="#fff" stroke-width="1.5"/>
    <circle cx="282" cy="217" r="9" fill="none" stroke="#fff" stroke-width="1.5"/><path d="M282 212 V217 H286" stroke="#fff" stroke-width="1.5" fill="none"/>
    <rect x="226" y="133" width="18" height="15" fill="none" stroke="#fff" stroke-width="1.5"/><path d="M226 139 H244" stroke="#fff" stroke-width="1.5"/>
    <g stroke="var(--navy)" stroke-width="1" fill="none"><path d="M358 126 V95 H364"/><path d="M340 230 Q352 236 364 230"/><path d="M212 135 V121 H206"/></g>
    <circle cx="359" cy="95" r="3.5" fill="var(--navy)"/>
    <circle cx="359" cy="231" r="3.5" fill="var(--yellow)"/>
    <circle cx="206" cy="118" r="3.5" fill="var(--teal)"/>
  </svg>
  <div class="info-text" style="left:370px;top:87px;width:135px"><h3>Title <b>One</b></h3>Lorem ipsum dolor sit amet, consectetur adipiscing elit. Vivamus eu dui ex. Curabitur dapibus</div>
  <div class="info-text" style="left:370px;top:224px;width:135px"><h3>Title <b>Two</b></h3>Lorem ipsum dolor sit amet, consectetur adipiscing elit. Vivamus eu dui ex. Curabitur dapibus</div>
  <div class="info-text" style="left:58px;top:110px;width:140px;text-align:right"><h3>Title <b>Three</b></h3>Lorem ipsum dolor sit amet, consectetur adipiscing elit. Vivamus eu dui ex. Curabitur dapibus</div>
  <div class="foot-brand brand"><span class="dot"></span><span class="name">Corvanta</span></div>
  <div class="foot-copy">© 2022 Corvanta Learning. All rights reserved.<span class="pg">7</span></div>
</section>

<!-- 8 table -->
<section class="slide col-r row-4">
  <h2 class="slide-title"><span><b>Table</b> Layout</span></h2>
  <table class="data-table">
    <thead><tr><th>Heading</th><th class="c1">Column Title 1</th><th class="c2">Column Title 2</th><th class="c3">Column Title 3</th><th class="c4">Column Title 4</th></tr></thead>
    <tbody>
      <tr><td>Feature One</td><td class="yes">✓</td><td class="yes">✓</td><td class="yes">✓</td><td class="yes">✓</td></tr>
      <tr><td>Feature Two</td><td class="yes">✓</td><td class="yes">✓</td><td class="yes">✓</td><td class="yes">✓</td></tr>
      <tr><td>Feature Three</td><td class="yes">✓</td><td class="yes">✓</td><td class="yes">✓</td><td class="no">✕</td></tr>
      <tr><td>Feature Four</td><td class="yes">✓</td><td class="yes">✓</td><td class="no">✕</td><td class="no">✕</td></tr>
      <tr><td>Feature Five</td><td class="yes">✓</td><td class="no">✕</td><td class="no">✕</td><td class="no">✕</td></tr>
    </tbody>
  </table>
  <div class="foot-brand brand"><span class="dot"></span><span class="name">Corvanta</span></div>
  <div class="foot-copy">© 2022 Corvanta Learning. All rights reserved.<span class="pg">8</span></div>
</section>

<!-- 9 chart -->
<section class="slide col-l row-5">
  <h2 class="slide-title"><span><b>Chart</b> Slide</span></h2>
  <svg class="chart" width="562" height="316" viewBox="0 0 562 316" font-family="Montserrat, sans-serif" font-size="6" fill="var(--grey)">
    <g stroke="#e3e3e3" stroke-width=".6">
      <line x1="66" y1="230" x2="282" y2="230"/><line x1="66" y1="205" x2="282" y2="205"/><line x1="66" y1="180" x2="282" y2="180"/>
      <line x1="66" y1="155" x2="282" y2="155"/><line x1="66" y1="130" x2="282" y2="130"/><line x1="66" y1="105" x2="282" y2="105"/><line x1="66" y1="80" x2="282" y2="80"/>
    </g>
    <g text-anchor="end"><text x="60" y="232">0</text><text x="60" y="207">1</text><text x="60" y="182">2</text><text x="60" y="157">3</text><text x="60" y="132">4</text><text x="60" y="107">5</text><text x="60" y="82">6</text></g>
    <g>
      <rect x="76" y="122" width="9" height="108" fill="var(--navy)"/><rect x="88" y="170" width="9" height="60" fill="var(--yellow)"/><rect x="100" y="180" width="9" height="50" fill="var(--teal)"/>
      <rect x="130" y="167" width="9" height="63" fill="var(--navy)"/><rect x="142" y="120" width="9" height="110" fill="var(--yellow)"/><rect x="154" y="180" width="9" height="50" fill="var(--teal)"/>
      <rect x="183" y="142" width="9" height="88" fill="var(--navy)"/><rect x="195" y="185" width="9" height="45" fill="var(--yellow)"/><rect x="207" y="155" width="9" height="75" fill="var(--teal)"/>
      <rect x="237" y="118" width="9" height="112" fill="var(--navy)"/><rect x="249" y="160" width="9" height="70" fill="var(--yellow)"/><rect x="261" y="105" width="9" height="125" fill="var(--teal)"/>
    </g>
    <g text-anchor="middle"><text x="92" y="242">Category 1</text><text x="146" y="242">Category 2</text><text x="199" y="242">Category 3</text><text x="253" y="242">Category 4</text></g>
  </svg>
  <div class="options">
    <div class="option"><div class="icon bg-navy"><svg viewBox="0 0 20 20"><circle cx="10" cy="10" r="7" fill="none" stroke="#fff" stroke-width="1.8"/><path d="M10 6 V10 H13" fill="none" stroke="#fff" stroke-width="1.8"/></svg></div><div><h3>Option <b>One</b></h3><p>Vivamus eu dui ex. Curabitur dapibus dignissim dui, in molest</p></div></div>
    <div class="option"><div class="icon bg-yellow"><svg viewBox="0 0 20 20"><rect x="4" y="5" width="12" height="8" fill="none" stroke="#fff" stroke-width="1.8"/><rect x="2" y="14" width="16" height="2" fill="#fff"/></svg></div><div><h3>Option <b>Two</b></h3><p>Vivamus eu dui ex. Curabitur dapibus dignissim dui, in molest</p></div></div>
    <div class="option"><div class="icon bg-teal"><svg viewBox="0 0 20 20"><circle cx="6" cy="8" r="2.5" fill="#fff"/><circle cx="14" cy="8" r="2.5" fill="#fff"/><circle cx="10" cy="7" r="3" fill="#fff"/><rect x="3" y="12" width="14" height="4" rx="2" fill="#fff"/></svg></div><div><h3>Option <b>Three</b></h3><p>Vivamus eu dui ex. Curabitur dapibus dignissim dui, in molest</p></div></div>
  </div>
  <div class="foot-brand brand"><span class="dot"></span><span class="name">Corvanta</span></div>
  <div class="foot-copy">© 2022 Corvanta Learning. All rights reserved.<span class="pg">9</span></div>
</section>

<!-- 10 contact -->
<section class="slide col-r row-5">
  <div class="photo contact-photo" role="img" aria-label="Upward photo of glass office towers against the sky"></div>
  <div class="contact-accent"></div>
  <div class="contact-brand brand"><span class="dot"></span><span class="name">Corvanta</span></div>
  <div class="contact-list">
    <h3>Contact Us</h3>
    <ul>
      <li><svg viewBox="0 0 10 10"><path d="M2 1 L4 1 L4.5 3 L3.5 4 Q4.5 6 6 6.5 L7 5.5 L9 6 L9 8 Q5 9 2 5 Q1 3 2 1 Z" fill="var(--navy)"/></svg>Phone Number Goes Here</li>
      <li><svg viewBox="0 0 10 10"><circle cx="5" cy="5" r="3.8" fill="none" stroke="var(--navy)" stroke-width="1.1"/><circle cx="5" cy="5" r="1.5" fill="none" stroke="var(--navy)" stroke-width="1.1"/></svg>E-Mail Address Goes Here</li>
      <li><svg viewBox="0 0 10 10"><circle cx="5" cy="5" r="4" fill="none" stroke="var(--navy)" stroke-width="1"/><ellipse cx="5" cy="5" rx="1.8" ry="4" fill="none" stroke="var(--navy)" stroke-width=".8"/><path d="M1 5 H9" stroke="var(--navy)" stroke-width=".8"/></svg>URL Address Goes Here</li>
    </ul>
  </div>
  <div class="copy-bar">© 2022 Corvanta Learning. All rights reserved.</div>
</section>

</body>
</html>
```